Webdesign für Sandstrahl-Anbieter
Zielgruppe
Wir sind ein Dienstleister und bieten Sandstrahlen im Lohn an. Unsere Zielgruppe sind einerseits Privatpersonen 99% Männlich, die Restaurieren, Autoschrauben oder Oldtimer fahren. Andererseits Industriekunden die Metallkonstruktionen vor dem Beschichten sandstrahlen lassen wollen. Wir müssen also einerseits professionell wirken um Industriekunden abzuholen, andererseits kann es auch etwas ausgefallener werden, wie auch schon unser logo zeigt.
Aufgabenstellung
Ich möchte eine simpel gehaltene Page, auf der man sich von oben nach unten durchscrollt. Oben das logo und eine Begrüßung, danach mit jeweils einem Bild linksbündig einige Unterpunkte mit jeweils ca. 4 Zeilen Text.
Es soll permanent rechts oben ein 'Kontakt' Button mitfahren, der die Nummer und Mailadresse anzeigt.

```html
<!DOCTYPE html>
<html lang="de">
<head>
<meta charset="utf-8">
<title>KORN-Strahltechnik – Startseite</title>
<link href="https://fonts.googleapis.com/css2?family=Roboto:wght@300;400;500&family=Poppins:wght@400&display=swap" rel="stylesheet">
<style>
  :root{
    --orange:#f27f1b;
    --ink:#2b2b2b;
    --text:#444;
    --white:#ffffff;
    --panel:#ececea;
    --header-band:rgba(245,245,245,.88);
  }
  *{box-sizing:border-box;margin:0;padding:0}
  html,body{width:1200px;height:960px;overflow:hidden;background:var(--white)}
  body{font-family:"Roboto",Arial,sans-serif;color:var(--ink);position:relative}

  .hero{position:absolute;left:0;top:0;width:1200px;height:560px;
    background:
      radial-gradient(ellipse at 55% 55%, #b9b9b9 0%, #8f8f8f 35%, transparent 70%),
      linear-gradient(180deg,#6f6f6f 0%,#9a9a9a 30%,#7a7a7a 65%,#4e4e4e 100%);}
  .site-header{position:absolute;left:0;top:0;width:1200px;height:84px;background:var(--header-band);
    display:flex;align-items:center;justify-content:space-between;padding:0 28px 0 92px}
  .brand{display:flex;align-items:center;gap:10px;font-weight:500;font-size:22px;letter-spacing:2px;color:var(--ink)}
  .brand-dot{width:14px;height:14px;border-radius:50%;background:var(--ink)}
  .main-nav{display:flex;gap:30px;font-size:19px;font-weight:400;text-transform:uppercase}
  .main-nav a{color:var(--ink);text-decoration:none}
  .main-nav a.active{color:var(--orange)}

  .hero-copy{position:absolute;left:0;top:318px;width:1200px;text-align:center;color:var(--white);
    text-shadow:0 2px 6px rgba(0,0,0,.55)}
  .hero-title{font-size:42px;font-weight:500;letter-spacing:.5px;text-transform:uppercase}
  .hero-sub{font-size:31px;font-weight:300;margin-top:4px}

  .contact-float{position:absolute;right:0;top:512px;display:flex;flex-direction:column;gap:4px}
  .contact-float span{width:44px;height:34px;background:var(--orange);display:flex;align-items:center;justify-content:center}

  .intro{position:absolute;top:600px;left:0;width:1200px;text-align:center}
  .intro h1{font-size:27px;font-weight:400;text-transform:uppercase;letter-spacing:.3px}
  .intro p{font-family:"Poppins",Arial,sans-serif;font-size:13px;line-height:21px;color:var(--text);width:520px;margin:26px auto 0}

  .service{position:absolute;top:780px;left:84px;width:1032px;height:410px;display:flex}
  .service-photo{width:600px;height:100%;background:radial-gradient(ellipse at 35% 50%,#8a8175 0%,#4a4641 45%,#2c2a28 100%)}
  .service-body{flex:1;background:var(--panel);padding:74px 52px 0 54px}
  .service-body h2{font-size:20px;font-weight:400;text-transform:uppercase;letter-spacing:.3px}
  .service-body p{font-family:"Poppins",Arial,sans-serif;font-size:12px;line-height:31px;color:var(--text);margin-top:30px}
</style>
</head>
<body>
  <div class="hero" role="img" aria-label="Schwarzweißfoto: gestrahlte Oldtimer-Karosserie in der Werkhalle"></div>

  <header class="site-header">
    <div class="brand"><span class="brand-dot"></span>KORN</div>
    <nav class="main-nav">
      <a class="active" href="#">Home</a>
      <a href="#">Leistungen</a>
      <a href="#">Über uns</a>
      <a href="#">Impressum</a>
      <a href="#">Kontakt</a>
    </nav>
  </header>

  <div class="hero-copy">
    <div class="hero-title">Strahlen für höchste Ansprüche</div>
    <div class="hero-sub">Von der Entlackung bis zur Restaurierung</div>
  </div>

  <div class="contact-float">
    <span aria-label="Telefon">
      <svg width="20" height="20" viewBox="0 0 24 24"><path d="M6.6 10.8c1.4 2.8 3.8 5.1 6.6 6.6l2.2-2.2c.3-.3.7-.4 1-.2 1.1.4 2.3.6 3.6.6.6 0 1 .4 1 1V20c0 .6-.4 1-1 1C10.6 21 3 13.4 3 4c0-.6.4-1 1-1h3.5c.6 0 1 .4 1 1 0 1.3.2 2.5.6 3.6.1.3 0 .7-.2 1L6.6 10.8z" fill="#fff"/></svg>
    </span>
    <span aria-label="E-Mail">
      <svg width="22" height="16" viewBox="0 0 22 16"><rect x="1" y="1" width="20" height="14" fill="none" stroke="#fff" stroke-width="1.6"/><path d="M1 1l10 8 10-8" fill="none" stroke="#fff" stroke-width="1.6"/></svg>
    </span>
  </div>

  <section class="intro">
    <h1>Lorem ipsum dolor sit amet</h1>
    <p>Ut enim ad minim veniam, quis nostrud exercitation ullamco laboris nisi ut aliquip ex ea commodo consequat. Duis aute irure dolor in reprehenderit in voluptate velit esse cillum dolore eu fugiat nulla pariatur.</p>
  </section>

  <article class="service">
    <div class="service-photo" role="img" aria-label="Nahaufnahme: verrostetes Blech mit freigestrahlter Stelle"></div>
    <div class="service-body">
      <h2>Entlacken/Entrosten</h2>
      <p>Amet purus gravida quis blandit turpis cursus in hac<br>
      Egestas diam in arcu cursus euismod quis viverra<br>
      Est ullamcorper eget nulla facilisi.<br>
      Dictum fusce ut placerat orci nulla pellentesque.</p>
    </div>
  </article>
</body>
</html>
```